Biz Card Design TPVC

New business card for a new company.
Logo was completed by a designer on ArtFlock and looking to continue requesting additional services.
Company Name: Tidal Prime Voltage Collective
Although this company is starting in Canada, we will be moving towards a global presence within the next 6 months.
Key elements to this business are as follows.
Energy Procurement
Energy Reduction Services
Demand Side Consulting
Energy Efficiency Consulting
Saving Clients Money
Helping Them Go "Green"
Managing Their Energy Requirements
Basically the goal for our company is to find the best procurement solution for our clients and reduce their energy consumption. This reduces their expenses and the amount of greenhouse gas they produce on a daily basis.
I have been in the energy footprint for the last 20 years and know that most companies are looking to "do whatever is necessary to get them to sign on the dotted line". I would prefer to walk away from a client that I can't help than to put them into a situation that they will regret for years to come. This is where the "TIDAL" part of the company name comes from.
The following is a catch phrase that encompasses what we do.
"Reducing your carbon footprint & energy bill at the same time!"
The back of the card needs to have this statement along with some sort of illustration. The back is a playground for creative ideas.
The front of the card needs the following.
Logo.
First & Last Name (Gus Marwick)
Title (Energy Warrior)
Phone Number (555) 314-2768
Fax Number (555) 862-4091
Email Address gus@tidalprimevoltage.example
Address 47 Orchard Lane Toronto Ontario K4P 2Z7
I want it to be a card that is remembered when any of my staff give it to a customer. It HAS to stand out.
Target Market(s)
Business Owners, Decision Makers, 30 to 65+
Industry/Entity Type
Business
Look and feel
Each slider illustrates characteristics of the customer's brand and the style your logo design should communicate.

```html
<!DOCTYPE html>
<html lang="en">
<head>
<meta charset="utf-8">
<title>Tidal Prime Voltage Collective — Business Card</title>
<link rel="stylesheet" href="https://fonts.googleapis.com/css2?family=Lato:ital,wght@0,300;0,400;0,700;1,400&family=Roboto+Condensed:wght@500&display=swap">
<style>
  :root {
    --canvas: #ecebe8;
    --card: #f6f6f4;
    --ink: #2b2b2b;
    --muted-ink: #555555;
    --brand-blue: #3f6db3;
    --band-blue: #4570b4;
    --leaf-green: #2f9a3c;
    --rule-green: #6cb56f;
    --photo-light: #e4e0da;
    --photo-dark: #b9aa9c;
  }
  * { box-sizing: border-box; margin: 0; padding: 0; }
  html, body { width: 1200px; height: 900px; overflow: hidden; }
  body {
    background: var(--canvas);
    font-family: "Lato", sans-serif;
    color: var(--ink);
    position: relative;
  }
  .card {
    position: absolute;
    background: var(--card);
    box-shadow: 0 6px 18px rgba(0,0,0,.16);
    overflow: hidden;
  }

  /* Back of card */
  .card-back { left: 110px; top: 170px; width: 320px; height: 560px; }
  .back-photo {
    position: absolute; left: 0; top: 0; width: 320px; height: 330px;
    background: linear-gradient(180deg, var(--photo-light) 0%, var(--photo-dark) 100%);
  }
  .back-band { position: absolute; left: 0; top: 290px; width: 320px; height: 270px; }
  .back-slogan {
    position: absolute; left: 24px; right: 14px; top: 392px;
    font-family: "Roboto Condensed", sans-serif;
    font-weight: 500; font-size: 20px; line-height: 1.35;
    color: #fff;
    white-space: nowrap;
  }

  /* Front of card */
  .card-front { left: 500px; top: 285px; width: 590px; height: 340px; }
  .brand {
    position: absolute; left: 44px; top: 60px;
    display: flex; align-items: center; gap: 12px;
  }
  .brand-dot { width: 22px; height: 22px; border-radius: 50%; background: var(--leaf-green); }
  .brand-name {
    font-weight: 700; font-size: 27px; color: var(--brand-blue); letter-spacing: -0.3px;
  }
  .person { position: absolute; left: 80px; top: 118px; }
  .person-name { font-weight: 400; font-size: 22px; letter-spacing: .5px; text-transform: uppercase; }
  .person-title { font-style: italic; font-size: 14px; color: var(--muted-ink); margin-top: 2px; }
  .divider {
    position: absolute; left: 80px; right: 40px; top: 196px;
    height: 1px; background: var(--rule-green);
  }
  .contact { position: absolute; left: 80px; top: 216px; font-size: 14px; line-height: 1.65; }
  .contact .label { color: var(--leaf-green); font-weight: 700; }
  .contact .sep { color: #888; padding: 0 8px; }
</style>
</head>
<body>

  <section class="card card-back" aria-label="Back of business card">
    <div class="back-photo" role="img" aria-label="Photo placeholder: a green seedling sprouting from a stack of gold coins in soil"></div>
    <svg class="back-band" viewBox="0 0 320 270" width="320" height="270" aria-hidden="true">
      <path d="M0 8 C 90 22, 220 40, 320 30 L320 270 L0 270 Z" fill="var(--band-blue)"/>
      <path d="M0 8 C 90 22, 220 40, 320 30" fill="none" stroke="var(--leaf-green)" stroke-width="9"/>
    </svg>
    <p class="back-slogan">Reducing your carbon footprint<br>&amp; energy bill at the same time!</p>
  </section>

  <section class="card card-front" aria-label="Front of business card">
    <div class="brand">
      <span class="brand-dot"></span>
      <span class="brand-name">Tidal Prime Voltage Collective</span>
    </div>
    <div class="person">
      <p class="person-name">Gus Marwick</p>
      <p class="person-title">Energy Warrior</p>
    </div>
    <div class="divider"></div>
    <div class="contact">
      <p><span class="label">T:</span> (555) 314-2768<span class="sep">|</span><span class="label">F:</span> (555) 862-4091</p>
      <p><span class="label">E:</span> gus@tidalprimevoltage.example</p>
      <p>47 Orchard Lane Toronto Ontario K4P 2Z7</p>
    </div>
  </section>

</body>
</html>
```